Business card for a doctor's practice

Would like a business card for a Pulmonary ( lung) doctor. I would like to include a logo with something in reference to air or oxygen or lungs. Would like the color red included somehow. Name of the company is Breathwell Medical Associates of Eastern Carolina and we specialize in Pulmonary Medicine,. I would like something streamlined and modern
Target Market(s)
Patients, hospitals, other doctors
Industry/Entity Type
Business
Contact Information for Business Card
Would like business details superimposed on a logo somehow
Look and feel

```html
<!DOCTYPE html>
<html lang="en">
<head>
<meta charset="utf-8">
<title>Breathwell Medical Associates – Business Card</title>
<link rel="stylesheet" href="https://fonts.googleapis.com/css2?family=Montserrat:wght@800&family=Questrial&display=swap">
<style>
  :root {
    --brand-red: #ec1f27;
    --frame-red: #e3262c;
    --paper-light: #ffffff;
    --paper-mid: #e9e9e9;
    --paper-edge: #dcdcdc;
    --strip-gray: #e6e6e6;
    --ink-white: #ffffff;
    --ink-muted: #8a8a8a;
  }
  html, body {
    margin: 0;
    padding: 0;
    width: 1200px;
    height: 652px;
    overflow: hidden;
    background: #ffffff;
  }
  .card {
    position: relative;
    width: 1200px;
    height: 652px;
    box-sizing: border-box;
    border: 2px solid var(--frame-red);
    background: radial-gradient(ellipse 70% 80% at 50% 40%, var(--paper-light) 0%, var(--paper-mid) 75%, var(--paper-edge) 100%);
    overflow: hidden;
    font-family: "Questrial", "Century Gothic", sans-serif;
  }
  .brand {
    position: absolute;
    left: 0;
    right: 0;
    top: 52px;
    text-align: center;
  }
  .brand-mark {
    display: block;
    margin: 0 auto 26px;
    width: 170px;
    height: 170px;
  }
  .brand-name {
    margin: 0;
    color: var(--brand-red);
    font-family: "Questrial", "Century Gothic", sans-serif;
    font-weight: 400;
    text-transform: uppercase;
    line-height: 1.2;
  }
  .brand-name .line-main {
    display: block;
    font-size: 38px;
    letter-spacing: 2px;
  }
  .brand-name .line-sub {
    display: block;
    font-size: 17px;
    letter-spacing: 9px;
    margin-top: 4px;
  }
  .info-band {
    position: absolute;
    left: 0;
    right: 0;
    top: 444px;
    height: 155px;
    background: var(--brand-red);
    color: var(--ink-white);
  }
  .bottom-strip {
    position: absolute;
    left: 0;
    right: 0;
    top: 599px;
    bottom: 0;
    background: var(--strip-gray);
  }
  .person {
    position: absolute;
    left: 72px;
    top: 34px;
  }
  .person-name {
    margin: 0;
    font-family: "Montserrat", "Arial Black", sans-serif;
    font-weight: 800;
    font-size: 41px;
    letter-spacing: 1px;
    text-transform: uppercase;
    line-height: 1.1;
    text-shadow: 2px 3px 3px rgba(0, 0, 0, 0.35);
  }
  .person-title {
    margin: 12px 0 0;
    font-size: 24px;
    line-height: 1.2;
    text-shadow: 1px 2px 2px rgba(0, 0, 0, 0.25);
  }
  .contact {
    position: absolute;
    right: 68px;
    top: 20px;
    margin: 0;
    text-align: right;
    font-size: 23px;
    line-height: 31px;
    font-style: normal;
    text-shadow: 1px 2px 2px rgba(0, 0, 0, 0.25);
  }
  .contact span { display: block; }
</style>
</head>
<body>
  <main class="card">
    <header class="brand">
      <svg class="brand-mark" viewBox="0 0 170 170" aria-hidden="true">
        <circle cx="85" cy="85" r="85" fill="var(--brand-red)"/>
      </svg>
      <h1 class="brand-name">
        <span class="line-main">Breathwell Medical Associates</span>
        <span class="line-sub">of Eastern Carolina</span>
      </h1>
    </header>

    <section class="info-band">
      <div class="person">
        <h2 class="person-name">Daniel R. Ashford</h2>
        <p class="person-title">Chest Disease Specialist</p>
      </div>
      <address class="contact">
        <span>4120 Magnolia Ridge Dr, NC, 27858</span>
        <span>(252) 555-0142 - (252) 555-0143</span>
        <span>info@breathwellmed.com</span>
        <span>www.breathwellmed.com</span>
      </address>
    </section>

    <div class="bottom-strip"></div>
  </main>
</body>
</html>
```